Crypto Exchange Comparison Platform

Let’s design a page that lets users compare hundreds of cryptocurrency exchanges. It will help users compare more info than anywhere else so you can find the best crypto exchange for your needs. The goal is to transform complex data into a clean, visually engaging experience.

Key Features to Design:
- Interactive comparison table with ~ 30 columns
- Filters and dropdown menus for easier usability
- Summary boxes for quick-view statistics
- Visual charts and graphs for key metrics
- Web, mobile, and tablet responsive design

Design Goals:
- Clean, modern aesthetic that makes complex data easily digestible
- Interactive elements (eg. Bar and Spider charts) for user engagement
- "Screenshot-friendly" sections for social media and sharing
- Data visualization focus (charts, graphs, metrics)
- Extremely easy to use on mobile
- Designs that use the color green
- A brand that communicates research and trusted information

Deliverables:
- High-fidelity mockup for desktop, tablet, and mobile versions
- Interactive prototype (Figma preferred)
- Style guide (typography, colors, components)

Note: The goal is to create an intuitive, visually engaging tool that helps users compare cryptocurrency exchanges efficiently while maintaining a clean, professional appearance that works well for social media sharing and content creation.
Updates

Low design quality

Industry/Entity Type

FinTech, Crypto, Finance

Number of Pages Required

1 page

Font styles to use
Other font styles liked:
• Inter or something good for a finance/data related website site

Colors
00AB8E
00BBA5
67D7C9
C6EFE9
E9F9F6

Requirements
Must have
• Please refer to the sketch I uploaded

```html
<!DOCTYPE html>
<html lang="en">
<head>
<meta charset="utf-8">
<title>Compare Crypto Exchanges – Design System &amp; Layouts</title>
<link rel="stylesheet" href="https://fonts.googleapis.com/css2?family=Inter:wght@400;500;600;700;800&display=swap">
<style>
:root{
  --green:#3dae84;
  --green-2:#00bba5;
  --mint:#c6efe9;
  --mint-pale:#e9f9f6;
  --black:#000;
  --ink:#1c1c1c;
  --ink-2:#444;
  --muted:#8a8a8a;
  --line:#e7e7e7;
  --page:#f6f6f6;
  --white:#fff;
  --board:#575757;
}
*{box-sizing:border-box;margin:0;padding:0}
html,body{width:1200px;height:1011px;overflow:hidden;background:var(--board)}
body{font-family:"Inter",sans-serif;color:var(--ink)}
.board{position:relative;width:2094px;height:1764px;transform:scale(.57306);transform-origin:0 0}
.artboard{position:absolute;background:var(--page);overflow:hidden}
.abs{position:absolute}
/* style guide */
.guide{left:46px;top:104px;width:582px;height:1232px;background:var(--white)}
.guide-label{position:absolute;left:23px;font-size:8px;font-weight:600}
.swatch{position:absolute;width:101px;height:91px;border-radius:4px}
.guide-meta{position:absolute;left:23px;font-size:6px;color:var(--ink-2)}
.guide-h1{position:absolute;left:23px;top:350px;font-size:20px;font-weight:700;line-height:20px;color:var(--ink-2)}
.guide-h2{position:absolute;left:23px;top:437px;font-size:9px;color:var(--ink-2)}
.guide-body{position:absolute;left:23px;width:285px;font-size:5.5px;line-height:8px;color:var(--ink-2)}
.mini-table{position:absolute;left:23px;top:656px;width:289px;border:1px solid var(--line);font-size:4.5px;border-collapse:collapse}
.mini-table td,.mini-table th{height:16px;padding:0 6px;text-align:left;border-bottom:1px solid var(--line)}
.mini-table th{font-weight:600}
.mini-table td+td,.mini-table th+th{border-left:1px solid var(--line)}
.mini-table .hl{background:#eef2f5}
.components{position:absolute;left:23px;top:787px;width:537px;height:411px;border:1px dashed #c9a3f2;padding:8px}
.comp-card{background:var(--page);border-radius:4px;padding:0 0 4px;margin-bottom:10px}
/* data tables */
.table-card{background:var(--white);border-radius:6px;overflow:hidden}
.data-table{width:100%;border-collapse:collapse;font-size:4.6px;color:var(--ink)}
.data-table th{background:var(--mint-pale);color:var(--green);font-weight:500;height:23px;line-height:5.5px;padding:0 2px}
.data-table td{height:20px;text-align:center;border-bottom:1px solid var(--line)}
.data-table th:first-child,.data-table td:first-child{text-align:left;padding-left:10px}
.data-table .site{text-decoration:underline}
.ex-dot{display:inline-block;width:4px;height:4px;border-radius:50%;background:var(--green-2);margin-right:4px;vertical-align:middle}
.table-foot{display:flex;justify-content:space-between;font-size:4.6px;color:var(--ink-2);padding:8px 10px 6px}
.table-foot .more{color:var(--green)}
/* desktop */
.desktop{top:104px;width:604px;height:1555px}
.site-header{position:absolute;left:0;top:0;width:100%;height:40px;background:var(--white)}
.logo{position:absolute;font-weight:500;color:var(--green)}
.desktop .logo{left:33px;top:12px;font-size:12px}
.nav{position:absolute;right:33px;top:17px;font-size:4.5px;color:var(--ink-2);display:flex;gap:18px}
.updated{position:absolute;font-weight:600;color:var(--ink)}
.title{position:absolute;font-weight:800;letter-spacing:.3px;color:var(--black)}
.tracked{position:absolute;color:var(--ink-2)}
.tracked b{color:var(--green);font-weight:700}
.btn{position:absolute;background:var(--green);color:var(--white);font-weight:600;display:flex;align-items:center;justify-content:center;gap:3px}
.rating-badge{position:absolute;background:var(--mint);border-radius:3px}
.divider{position:absolute;height:1px;background:#dcdcdc}
.section-title{position:absolute;font-weight:600;color:var(--black)}
.pick{position:absolute;background:var(--green);border-radius:4px;color:var(--white)}
.pick .name{position:absolute;font-weight:600}
.pick .arrow{position:absolute}
.pick .meta{position:absolute;display:flex;justify-content:space-between;font-weight:500}
.tabs{position:absolute;display:flex;gap:14px;font-size:6.5px;color:var(--ink-2)}
.tabs .on{color:var(--green);border-bottom:1.5px solid var(--green);padding-bottom:3px}
.tools{position:absolute;display:flex;gap:4px}
.tool{border:1px solid #d5d5d5;border-radius:2px;background:var(--white);font-size:5px;color:var(--ink-2);height:13px;padding:0 6px;display:flex;align-items:center;gap:4px}
.card{position:absolute;background:var(--white);border-radius:6px}
.chart-label{position:absolute;font-size:5.5px;font-weight:500;left:12px;top:10px}
.stat{position:absolute;background:var(--white);border-radius:6px;text-align:center}
.stat .k{color:var(--muted)}
.stat .v{color:var(--green);font-weight:500}
.select{position:absolute;border:1px solid #d8d8d8;border-radius:2px;display:flex;align-items:center;justify-content:space-between;padding:0 8px;font-weight:600;color:var(--ink)}
.acc-head{position:absolute;display:flex;justify-content:space-between;font-weight:600;color:var(--ink)}
.kv{position:absolute;display:grid;grid-template-columns:1.6fr 1fr .5fr;color:var(--ink)}
.see-all{position:absolute;background:var(--green);color:var(--white);display:flex;align-items:center;justify-content:center;font-weight:600}
.radar-table{position:absolute;border-collapse:collapse}
.radar-table td,.radar-table th{text-align:center;border-bottom:1px solid var(--line)}
.radar-table td:first-child{text-align:left;font-weight:600}
.faq-zone{position:absolute;left:0;width:100%;background:var(--white)}
.faq{position:absolute;background:var(--page);border-radius:6px}
.faq .q{position:absolute;font-weight:600;display:flex;justify-content:space-between}
.faq .a{position:absolute;color:var(--ink-2)}
.footer{position:absolute;display:flex;justify-content:space-between;color:var(--muted)}
.dropdown{position:absolute;left:415px;top:374px;width:94px;height:206px;background:var(--white);border-radius:3px;box-shadow:0 2px 8px rgba(0,0,0,.18);padding:6px 8px;font-size:4.5px;color:var(--ink-2)}
.dropdown li{list-style:none;height:14.6px;display:flex;align-items:center;gap:4px}
.dropdown li.on{color:var(--green)}
.box{width:4px;height:4px;border:.6px solid #ccc;border-radius:1px}
.on .box{background:var(--green);border-color:var(--green)}
.dropdown .apply{position:absolute;left:8px;right:8px;bottom:6px;height:11px;background:var(--green);color:var(--white);font-size:4px;display:flex;align-items:center;justify-content:center}
/* mobile */
.mobile{left:1884px;top:104px;width:163px;height:1398px}
.mobile .site-header{height:28px}
.mobile .logo{left:9px;top:9px;font-size:7.5px}
.burger{position:absolute;right:9px;top:10px;width:7px;height:6px;border-top:1px solid var(--ink);border-bottom:1px solid var(--ink)}
.burger:after{content:"";position:absolute;left:0;right:0;top:1.8px;height:1px;background:var(--ink)}
</style>
</head>
<body>
<div class="board">

<!-- ================= STYLE GUIDE ================= -->
<section class="artboard guide">
  <div class="guide-label" style="top:34px">Colors</div>
  <div class="swatch" style="left:23px;top:58px;background:var(--green)"></div>
  <div class="swatch" style="left:130px;top:58px;background:var(--mint)"></div>
  <div class="swatch" style="left:238px;top:58px;background:var(--mint)"></div>
  <div class="swatch" style="left:345px;top:58px;background:var(--mint-pale)"></div>
  <div class="swatch" style="left:452px;top:58px;background:var(--black)"></div>
  <div class="swatch" style="left:23px;top:155px;background:#474747"></div>
  <div class="swatch" style="left:130px;top:155px;background:var(--white);border:1px solid var(--line)"></div>
  <div class="swatch" style="left:238px;top:155px;background:#ececec"></div>

  <div class="guide-label" style="top:292px">Typography</div>
  <div class="guide-meta" style="top:323px;font-size:10px">h1</div>
  <div class="guide-h1">Taxing Laughter: The Joke<br>Tax Chronicles</div>
  <div class="guide-meta" style="top:410px;font-size:9px">h2</div>
  <div class="guide-h2">The People of the Kingdom</div>
  <div class="guide-meta" style="top:468px">h3</div>
  <div class="guide-meta" style="top:491px;color:var(--ink)">The Joke Tax</div>
  <div class="guide-meta" style="top:520px">body 1</div>
  <div class="guide-body" style="top:543px">The king, seeing how much happier his subjects were, realized the error of his ways and repealed the joke tax.</div>
  <div class="guide-meta" style="top:580px">body 2</div>
  <div class="guide-body" style="top:601px;font-size:4.8px;line-height:6px">The king, seeing how much happier his subjects were, realized the error of his ways and repealed the joke tax.</div>
  <div class="guide-meta" style="top:636px">Table</div>
  <table class="mini-table">
    <tr><th>King's Treasury</th><th>People's happiness</th></tr>
    <tr><td>Empty</td><td>Overflowing</td></tr>
    <tr class="hl"><td>Modest</td><td>Satisfied</td></tr>
    <tr><td>Empty</td><td>Overflowing</td></tr>
  </table>

  <div class="guide-label" style="top:765px">Components</div>
  <div class="components">
    <div class="comp-card">
      <table class="data-table">
        <tr><th>Exchanges</th><th>Last Updated</th><th>Visit</th><th>Maker Fee</th><th>Taker Fee</th><th>Futures<br>Maker Fee</th><th>Futures<br>Taker Fee</th><th>Trading Fee<br>Discount</th><th>Discount or<br>Bonus</th></tr>
        <tr><td><i class="ex-dot"></i>Bintrove</td><td>25 Feb 2025</td><td class="site">Go to site</td><td>0.10%</td><td>0.20%</td><td>0.20%</td><td>0.20%</td><td>No</td><td>$1000 Bonus</td></tr>
        <tr><td><i class="ex-dot"></i>Byvault</td><td>25 Feb 2025</td><td class="site">Go to site</td><td>0.10%</td><td>0.20%</td><td>0.20%</td><td>0.20%</td><td>No</td><td>$1000 Bonus</td></tr>
        <tr><td><i class="ex-dot"></i>Coinlane</td><td>25 Feb 2025</td><td class="site">Go to site</td><td>0.10%</td><td>0.20%</td><td>0.20%</td><td>0.20%</td><td>No</td><td>$1000 Bonus</td></tr>
        <tr><td><i class="ex-dot"></i>Oktrix</td><td>25 Feb 2025</td><td class="site">Go to site</td><td>0.10%</td><td>0.20%</td><td>0.20%</td><td>0.20%</td><td>No</td><td>$1000 Bonus</td></tr>
        <tr><td><i class="ex-dot"></i>Upnest</td><td>25 Feb 2025</td><td class="site">Go to site</td><td>0.10%</td><td>0.20%</td><td>0.20%</td><td>0.20%</td><td>No</td><td>$1000 Bonus</td></tr>
        <tr><td><i class="ex-dot"></i>Vextra</td><td>25 Feb 2025</td><td class="site">Go to site</td><td>0.10%</td><td>0.20%</td><td>0.20%</td><td>0.20%</td><td>No</td><td>$1000 Bonus</td></tr>
        <tr><td><i class="ex-dot"></i>Kuvion</td><td>25 Feb 2025</td><td class="site">Go to site</td><td>0.10%</td><td>0.20%</td><td>0.20%</td><td>0.20%</td><td>No</td><td>$1000 Bonus</td></tr>
      </table>
      <div class="table-foot"><span>Showing 1 to 7 of 120 Results</span><span class="more">Show more</span></div>
    </div>
    <div class="comp-card">
      <table class="data-table">
        <tr><th>Exchanges</th><th>Last Updated</th><th>Visit</th><th>Number of<br>Coins</th><th>Number of<br>Futures</th><th>Max<br>Leverage</th><th>Fiat<br>Currencies</th><th>Margins</th><th>Copy Trading</th><th>Trading Bots</th><th>P2P Trading</th></tr>
        <tr><td><i class="ex-dot"></i>Bintrove</td><td>25 Feb 2025</td><td class="site">Go to site</td><td>0.10%</td><td>0.20%</td><td>45x</td><td>7</td><td>5x</td><td>Yes</td><td>Yes</td><td>Yes</td></tr>
        <tr><td><i class="ex-dot"></i>Byvault</td><td>25 Feb 2025</td><td class="site">Go to site</td><td>0.10%</td><td>0.20%</td><td>100x</td><td>5</td><td>3x</td><td>Yes</td><td>Yes</td><td>Yes</td></tr>
        <tr><td><i class="ex-dot"></i>Coinlane</td><td>25 Feb 2025</td><td class="site">Go to site</td><td>0.10%</td><td>0.20%</td><td>20x</td><td>7</td><td>6x</td><td>Yes</td><td>Yes</td><td>No</td></tr>
        <tr><td><i class="ex-dot"></i>Oktrix</td><td>25 Feb 2025</td><td class="site">Go to site</td><td>0.10%</td><td>0.20%</td><td>20x</td><td>9</td><td>2x</td><td>Yes</td><td>Yes</td><td>Yes</td></tr>
        <tr><td><i class="ex-dot"></i>Upnest</td><td>25 Feb 2025</td><td class="site">Go to site</td><td>0.10%</td><td>0.20%</td><td>45x</td><td>10</td><td>NA</td><td>Yes</td><td>Yes</td><td>No</td></tr>
        <tr><td><i class="ex-dot"></i>Vextra</td><td>25 Feb 2025</td><td class="site">Go to site</td><td>0.10%</td><td>0.20%</td><td>45x</td><td>8</td><td>NA</td><td>Yes</td><td>Yes</td><td>No</td></tr>
        <tr><td><i class="ex-dot"></i>Kuvion</td><td>25 Feb 2025</td><td class="site">Go to site</td><td>0.10%</td><td>0.20%</td><td>45x</td><td>10</td><td>2x</td><td>No</td><td>Yes</td><td>Yes</td></tr>
      </table>
      <div class="table-foot"><span>Showing 1 to 7 of 120 Results</span><span class="more">Show more</span></div>
    </div>
  </div>
</section>

<!-- ================= DESKTOP (columns menu open) ================= -->
<section class="artboard desktop" style="left:644px">
  <header class="site-header"><div class="logo">Brand Logo</div><nav class="nav"><span>HOW WE TEST?</span><span>ABOUT</span></nav></header>
  <div class="updated" style="left:42px;top:63px;font-size:6px">UPDATED: 22 FEB, 2025</div>
  <h1 class="title" style="left:42px;top:80px;font-size:29px;line-height:33px">COMPARE CRYPTO<br>EXCHANGES</h1>
  <div class="tracked" style="left:42px;top:150px;font-size:12px">Platform Tracked: <b>125</b></div>
  <div class="btn" style="left:42px;top:176px;width:74px;height:20px;font-size:5px">HOW WE TEST? <span>↗</span></div>
  <div class="rating-badge" style="left:494px;top:66px;width:64px;height:26px" role="img" aria-label="Review rating badge"></div>
  <div class="divider" style="left:42px;top:222px;width:520px"></div>
  <h2 class="section-title" style="left:42px;top:247px;font-size:10px">Top Picks</h2>
  <div class="pick" style="left:42px;top:270px;width:166px;height:52px"><span class="name" style="left:10px;top:11px;font-size:12px">Vextra</span><svg class="arrow" style="right:12px;top:13px" width="12" height="12" viewBox="0 0 12 12"><path d="M2 10L10 2M4 2h6v6" stroke="#fff" stroke-width="1.4" fill="none"/></svg><div class="meta" style="left:10px;right:8px;bottom:9px;font-size:5px"><span>Trust score: 10/10</span><span>Go to the Platform</span></div></div>
  <div class="pick" style="left:218px;top:270px;width:166px;height:52px"><span class="name" style="left:10px;top:11px;font-size:12px">Coinlane</span><svg class="arrow" style="right:12px;top:13px" width="12" height="12" viewBox="0 0 12 12"><path d="M2 10L10 2M4 2h6v6" stroke="#fff" stroke-width="1.4" fill="none"/></svg><div class="meta" style="left:10px;right:8px;bottom:9px;font-size:5px"><span>Trust score: 10/10</span><span>Go to the Platform</span></div></div>
  <div class="pick" style="left:395px;top:270px;width:166px;height:52px"><span class="name" style="left:10px;top:11px;font-size:12px">Bintrove</span><svg class="arrow" style="right:12px;top:13px" width="12" height="12" viewBox="0 0 12 12"><path d="M2 10L10 2M4 2h6v6" stroke="#fff" stroke-width="1.4" fill="none"/></svg><div class="meta" style="left:10px;right:8px;bottom:9px;font-size:5px"><span>Trust score: 10/10</span><span>Go to the Platform</span></div></div>

  <div class="tabs" style="left:44px;top:355px"><span>Fees</span><span class="on">Features</span><span>Security</span></div>
  <div class="tools" style="right:42px;top:352px"><div class="tool">Columns <span>▯</span></div><div class="tool">Compare <span>⌄</span></div></div>
  <div class="table-card abs" style="left:42px;top:378px;width:520px">
    <table class="data-table">
      <tr><th>Exchanges</th><th>Last Updated</th><th>Visit</th><th>Number of<br>Coins</th><th>Number of<br>Futures</th><th>Max<br>Leverage</th><th>Fiat<br>Currencies</th><th>Margins</th><th>Copy Trading</th><th>Trading Bots</th><th>P2P Trading</th></tr>
      <tr><td><i class="ex-dot"></i>Bintrove</td><td>25 Feb 2025</td><td class="site">Go to site</td><td>0.10%</td><td>0.20%</td><td>45x</td><td>7</td><td>5x</td><td>Yes</td><td>Yes</td><td>Yes</td></tr>
      <tr><td><i class="ex-dot"></i>Byvault</td><td>25 Feb 2025</td><td class="site">Go to site</td><td>0.10%</td><td>0.20%</td><td>100x</td><td>5</td><td>3x</td><td>Yes</td><td>Yes</td><td>Yes</td></tr>
      <tr><td><i class="ex-dot"></i>Coinlane</td><td>25 Feb 2025</td><td class="site">Go to site</td><td>0.10%</td><td>0.20%</td><td>20x</td><td>7</td><td>6x</td><td>Yes</td><td>Yes</td><td>No</td></tr>
      <tr><td><i class="ex-dot"></i>Oktrix</td><td>25 Feb 2025</td><td class="site">Go to site</td><td>0.10%</td><td>0.20%</td><td>20x</td><td>9</td><td>2x</td><td>Yes</td><td>Yes</td><td>Yes</td></tr>
      <tr><td><i class="ex-dot"></i>Upnest</td><td>25 Feb 2025</td><td class="site">Go to site</td><td>0.10%</td><td>0.20%</td><td>45x</td><td>10</td><td>NA</td><td>Yes</td><td>Yes</td><td>No</td></tr>
      <tr><td><i class="ex-dot"></i>Vextra</td><td>25 Feb 2025</td><td class="site">Go to site</td><td>0.10%</td><td>0.20%</td><td>45x</td><td>8</td><td>NA</td><td>Yes</td><td>Yes</td><td>No</td></tr>
      <tr><td><i class="ex-dot"></i>Kuvion</td><td>25 Feb 2025</td><td class="site">Go to site</td><td>0.10%</td><td>0.20%</td><td>45x</td><td>10</td><td>2x</td><td>No</td><td>Yes</td><td>Yes</td></tr>
    </table>
    <div class="table-foot"><span>Showing 1 to 7 of 120 Results</span><span class="more">Show more</span></div>
  </div>
  <ul class="dropdown">
    <li class="on"><i class="box"></i>Number of Coins</li><li><i class="box"></i>Number of Futures</li><li><i class="box"></i>Max Leverage</li><li><i class="box"></i>Fiat Currencies</li><li><i class="box"></i>Margins</li><li><i class="box"></i>Copy Trading</li><li><i class="box"></i>Trading Bots</li><li><i class="box"></i>P2P Trading</li><li><i class="box"></i>Crypto Loans</li><li><i class="box"></i>Staking</li><li><i class="box"></i>Mobile Apps</li><li><i class="box"></i>24/7 Support</li>
    <div class="apply">APPLY</div>
  </ul>

  <div class="card" style="left:42px;top:586px;width:257px;height:122px">
    <div class="chart-label">Marker Fee ⌄</div>
    <svg class="abs" style="left:10px;top:30px" width="240" height="80" viewBox="0 0 240 80">
      <line x1="2" y1="7" x2="226" y2="7" stroke="#444" stroke-dasharray="2 2" stroke-width=".7"/><text x="228" y="9" font-size="4" font-weight="700">MAX</text>
      <g fill="#dedede"><rect x="2" y="52" width="11" height="18"/><rect x="22" y="26" width="11" height="44"/><rect x="42" y="40" width="11" height="30"/><rect x="62" y="34" width="11" height="36"/><rect x="82" y="30" width="11" height="40"/><rect x="122" y="48" width="11" height="22"/><rect x="142" y="26" width="11" height="44"/><rect x="162" y="58" width="11" height="12"/><rect x="182" y="36" width="11" height="34"/><rect x="202" y="52" width="11" height="18"/><rect x="222" y="40" width="11" height="30"/></g>
      <rect x="102" y="20" width="11" height="50" fill="var(--green)"/>
      <g font-size="3" fill="#999"><text x="4" y="78">Jan</text><text x="24" y="78">Feb</text><text x="44" y="78">Mar</text><text x="64" y="78">Apr</text><text x="84" y="78">May</text><text x="104" y="78">Jun</text><text x="124" y="78">Jul</text><text x="144" y="78">Aug</text><text x="164" y="78">Sep</text><text x="184" y="78">Oct</text><text x="204" y="78">Nov</text><text x="224" y="78">Dec</text></g>
    </svg>
  </div>
  <div class="card" style="left:309px;top:586px;width:253px;height:122px">
    <div class="chart-label">Trading Volume ⌄</div>
    <svg class="abs" style="left:8px;top:28px" width="240" height="84" viewBox="0 0 240 84">
      <polyline fill="none" stroke="var(--green)" stroke-width="1" points="0,42 8,36 14,30 22,44 30,50 36,38 44,28 52,46 58,40 66,34 74,48 80,42 88,46 96,36 104,44 112,40 120,46 128,34 136,44 144,38 152,40 160,44 168,32 176,38 184,30 192,36 200,28 208,40 214,34 220,6 226,30"/>
      <g font-size="3" fill="#999"><text x="230" y="5">$20K</text><text x="230" y="18">$15.6K</text><text x="230" y="31">$10K</text><text x="230" y="44">$5K</text><text x="230" y="57">$1.5K</text><text x="230" y="70">$1K</text>
      <text x="0" y="82">00:00</text><text x="28" y="82">03:00</text><text x="56" y="82">06:00</text><text x="84" y="82">09:00</text><text x="112" y="82">12:00</text><text x="140" y="82">15:00</text><text x="168" y="82">18:00</text><text x="196" y="82">21:00</text><text x="222" y="82">24:00</text></g>
    </svg>
  </div>
  <div class="stat" style="left:42px;top:715px;width:126px;height:54px"><div class="k" style="font-size:5px;margin-top:12px">Exchanges Tracked</div><div class="v" style="font-size:17px;margin-top:4px">125</div></div>
  <div class="stat" style="left:173px;top:715px;width:126px;height:54px"><div class="k" style="font-size:5px;margin-top:12px">Average Trading Fee</div><div class="v" style="font-size:17px;margin-top:4px">0.15%</div></div>
  <div class="stat" style="left:304px;top:715px;width:126px;height:54px"><div class="k" style="font-size:5px;margin-top:12px">Total Users</div><div class="v" style="font-size:17px;margin-top:4px">828 M</div></div>
  <div class="stat" style="left:435px;top:715px;width:126px;height:54px"><div class="k" style="font-size:5px;margin-top:12px">Web Visitors</div><div class="v" style="font-size:17px;margin-top:4px">12.2 B</div></div>

  <h2 class="section-title" style="left:42px;top:788px;font-size:10px">Compare</h2>
  <div class="card" style="left:42px;top:811px;width:520px;height:357px">
    <svg class="abs" style="left:0;top:0" width="260" height="240" viewBox="0 0 260 240">
      <g transform="translate(126 135)" fill="none" stroke="#e2e2e2" stroke-width=".6">
        <polygon points="0,-90 85.6,-27.8 52.9,72.8 -52.9,72.8 -85.6,-27.8"/>
        <polygon transform="scale(.75)" points="0,-90 85.6,-27.8 52.9,72.8 -52.9,72.8 -85.6,-27.8"/>
        <polygon transform="scale(.5)" points="0,-90 85.6,-27.8 52.9,72.8 -52.9,72.8 -85.6,-27.8"/>
        <polygon transform="scale(.25)" points="0,-90 85.6,-27.8 52.9,72.8 -52.9,72.8 -85.6,-27.8"/>
        <path d="M0 0L0-90M0 0L85.6-27.8M0 0L52.9 72.8M0 0L-52.9 72.8M0 0L-85.6-27.8"/>
        <polygon points="0,-52 62,-20 34,44 -44,62 -74,-20" fill="#d6f0e6" stroke="#a9dcc7"/>
        <polygon points="0,-66 90,-22 14,-4 46,64 -30,-4" fill="#8fd2b6" fill-opacity=".85" stroke="#6cc39f"/>
      </g>
      <g font-size="4" fill="#444"><text x="118" y="40">Security</text><text x="222" y="104">Features</text><text x="188" y="221">Deposits</text><text x="42" y="220">Withdrawals</text><text x="22" y="101">Fees</text></g>
    </svg>
    <table class="radar-table" style="left:26px;top:240px;width:194px;font-size:4.5px">
      <tr><th style="height:14px"></th><th>Bintrove</th><th>Coinlane</th></tr>
      <tr><td style="height:16.5px">Fees</td><td>xyz</td><td>xyz</td></tr><tr><td style="height:16.5px">Security</td><td>xyz</td><td>xyz</td></tr><tr><td style="height:16.5px">Features</td><td>xyz</td><td>xyz</td></tr><tr><td style="height:16.5px">Deposits</td><td>xyz</td><td>xyz</td></tr><tr><td style="height:16.5px">Withdrawals</td><td>xyz</td><td>xyz</td></tr>
    </table>
    <div class="select" style="left:282px;top:38px;width:103px;height:21px;font-size:7px"><span>Bintrove</span><span>⌄</span></div>
    <div class="select" style="left:390px;top:38px;width:99px;height:21px;font-size:7px"><span>Coinlane</span><span>⌄</span></div>
    <div class="acc-head" style="left:286px;top:86px;width:200px;font-size:6px"><span>Top Picks</span><span>⌃</span></div>
    <div class="kv" style="left:286px;top:109px;width:196px;font-size:4.5px;row-gap:10px"><span># of Coins</span><span>xyz</span><span>xyz</span><span># of Futures</span><span>xyz</span><span>xyz</span><span>Trading Bots</span><span>xyz</span><span>xyz</span><span>Copy Bots</span><span>xyz</span><span>xyz</span><span>24/7 Support</span><span>xyz</span><span>xyz</span></div>
    <div class="divider" style="left:282px;top:195px;width:207px"></div>
    <div class="acc-head" style="left:286px;top:207px;width:200px;font-size:6px"><span>Security</span><span>⌄</span></div>
    <div class="acc-head" style="left:286px;top:231px;width:200px;font-size:6px"><span>Fees</span><span>⌄</span></div>
    <div class="acc-head" style="left:286px;top:254px;width:200px;font-size:6px"><span>Deposits</span><span>⌄</span></div>
    <div class="acc-head" style="left:286px;top:277px;width:200px;font-size:6px"><span>Withdrawals</span><span>⌄</span></div>
    <div class="see-all" style="left:282px;top:313px;width:207px;height:21px;font-size:6px">See All</div>
  </div>

  <div class="faq-zone" style="top:1194px;height:328px">
    <h2 class="section-title" style="left:42px;top:44px;font-size:10px">Frequently asked Question</h2>
    <div class="faq" style="left:42px;top:68px;width:520px;height:55px"><div class="q" style="left:20px;right:20px;top:16px;font-size:6.5px"><span>What are the Crypto Exchanges?</span><span>⌃</span></div><div class="a" style="left:20px;top:35px;font-size:6px">All current paused or on-hold postings will expire end of 2024.</div></div>
    <div class="faq" style="left:42px;top:130px;width:520px;height:76px"><div class="q" style="left:20px;right:20px;top:15px;font-size:6.5px"><span>How to choose Crypto Exchanges?</span><span>⌃</span></div><div class="a" style="left:20px;right:20px;top:34px;font-size:6px;line-height:10.5px">For confidential postings on Jobwell job page there's a $250 hosting fee (as well as other incurred fees) to use Arbor' account, which will include our team's search for possible candidates on these hiring platforms when purchasing Basic or Standard packages (this is included in Deluxe packages upon requested).</div></div>
    <div class="faq" style="left:42px;top:213px;width:520px;height:37px"><div class="q" style="left:20px;right:20px;top:14px;font-size:6.5px"><span>How is data tracked?</span><span>⌃</span></div></div>
    <div class="faq" style="left:42px;top:257px;width:520px;height:37px"><div class="q" style="left:20px;right:20px;top:14px;font-size:6.5px"><span>How often is data updated?</span><span>⌃</span></div></div>
  </div>
  <div class="footer" style="left:33px;right:33px;top:1535px;font-size:4.5px"><span>Privacy Policy</span><span>©2025 All rights reserved</span></div>
</section>

<!-- ================= DESKTOP (fees tab) ================= -->
<section class="artboard desktop" style="left:1264px">
  <header class="site-header"><div class="logo">Brand Logo</div><nav class="nav"><span>HOW WE TEST?</span><span>ABOUT</span></nav></header>
  <div class="updated" style="left:42px;top:63px;font-size:6px">UPDATED: 22 FEB, 2025</div>
  <h1 class="title" style="left:42px;top:80px;font-size:29px;line-height:33px">COMPARE CRYPTO<br>EXCHANGES</h1>
  <div class="tracked" style="left:42px;top:150px;font-size:12px">Platform Tracked: <b>125</b></div>
  <div class="btn" style="left:42px;top:176px;width:74px;height:20px;font-size:5px">HOW WE TEST? <span>↗</span></div>
  <div class="rating-badge" style="left:494px;top:66px;width:64px;height:26px" role="img" aria-label="Review rating badge"></div>
  <div class="divider" style="left:42px;top:222px;width:520px"></div>
  <h2 class="section-title" style="left:42px;top:247px;font-size:10px">Top Picks</h2>
  <div class="pick" style="left:42px;top:270px;width:166px;height:52px"><span class="name" style="left:10px;top:11px;font-size:12px">Vextra</span><svg class="arrow" style="right:12px;top:13px" width="12" height="12" viewBox="0 0 12 12"><path d="M2 10L10 2M4 2h6v6" stroke="#fff" stroke-width="1.4" fill="none"/></svg><div class="meta" style="left:10px;right:8px;bottom:9px;font-size:5px"><span>Trust score: 10/10</span><span>Go to the Platform</span></div></div>
  <div class="pick" style="left:218px;top:270px;width:166px;height:52px"><span class="name" style="left:10px;top:11px;font-size:12px">Coinlane</span><svg class="arrow" style="right:12px;top:13px" width="12" height="12" viewBox="0 0 12 12"><path d="M2 10L10 2M4 2h6v6" stroke="#fff" stroke-width="1.4" fill="none"/></svg><div class="meta" style="left:10px;right:8px;bottom:9px;font-size:5px"><span>Trust score: 10/10</span><span>Go to the Platform</span></div></div>
  <div class="pick" style="left:395px;top:270px;width:166px;height:52px"><span class="name" style="left:10px;top:11px;font-size:12px">Bintrove</span><svg class="arrow" style="right:12px;top:13px" width="12" height="12" viewBox="0 0 12 12"><path d="M2 10L10 2M4 2h6v6" stroke="#fff" stroke-width="1.4" fill="none"/></svg><div class="meta" style="left:10px;right:8px;bottom:9px;font-size:5px"><span>Trust score: 10/10</span><span>Go to the Platform</span></div></div>

  <div class="tabs" style="left:44px;top:355px"><span class="on">Fees</span><span>Features</span><span>Security</span></div>
  <div class="tools" style="right:42px;top:352px"><div class="tool">Columns <span>▯</span></div><div class="tool">Compare <span>⌄</span></div></div>
  <div class="table-card abs" style="left:42px;top:378px;width:520px">
    <table class="data-table">
      <tr><th>Exchanges</th><th>Last Updated</th><th>Visit</th><th>Maker Fee</th><th>Taker Fee</th><th>Futures<br>Maker Fee</th><th>Futures<br>Taker Fee</th><th>Trading Fee<br>Discount</th><th>Discount or<br>Bonus</th></tr>
      <tr><td><i class="ex-dot"></i>Bintrove</td><td>25 Feb 2025</td><td class="site">Go to site</td><td>0.10%</td><td>0.20%</td><td>0.20%</td><td>0.20%</td><td>No</td><td>$1000 Bonus</td></tr>
      <tr><td><i class="ex-dot"></i>Byvault</td><td>25 Feb 2025</td><td class="site">Go to site</td><td>0.10%</td><td>0.20%</td><td>0.20%</td><td>0.20%</td><td>No</td><td>$1000 Bonus</td></tr>
      <tr><td><i class="ex-dot"></i>Coinlane</td><td>25 Feb 2025</td><td class="site">Go to site</td><td>0.10%</td><td>0.20%</td><td>0.20%</td><td>0.20%</td><td>No</td><td>$1000 Bonus</td></tr>
      <tr><td><i class="ex-dot"></i>Oktrix</td><td>25 Feb 2025</td><td class="site">Go to site</td><td>0.10%</td><td>0.20%</td><td>0.20%</td><td>0.20%</td><td>No</td><td>$1000 Bonus</td></tr>
      <tr><td><i class="ex-dot"></i>Upnest</td><td>25 Feb 2025</td><td class="site">Go to site</td><td>0.10%</td><td>0.20%</td><td>0.20%</td><td>0.20%</td><td>No</td><td>$1000 Bonus</td></tr>
      <tr><td><i class="ex-dot"></i>Vextra</td><td>25 Feb 2025</td><td class="site">Go to site</td><td>0.10%</td><td>0.20%</td><td>0.20%</td><td>0.20%</td><td>No</td><td>$1000 Bonus</td></tr>
      <tr><td><i class="ex-dot"></i>Kuvion</td><td>25 Feb 2025</td><td class="site">Go to site</td><td>0.10%</td><td>0.20%</td><td>0.20%</td><td>0.20%</td><td>No</td><td>$1000 Bonus</td></tr>
    </table>
    <div class="table-foot"><span>Showing 1 to 7 of 120 Results</span><span class="more">Show more</span></div>
  </div>

  <div class="card" style="left:42px;top:586px;width:257px;height:122px">
    <div class="chart-label">Marker Fee ⌄</div>
    <svg class="abs" style="left:10px;top:30px" width="240" height="80" viewBox="0 0 240 80">
      <line x1="2" y1="7" x2="226" y2="7" stroke="#444" stroke-dasharray="2 2" stroke-width=".7"/><text x="228" y="9" font-size="4" font-weight="700">MAX</text>
      <g fill="#dedede"><rect x="2" y="52" width="11" height="18"/><rect x="22" y="26" width="11" height="44"/><rect x="42" y="40" width="11" height="30"/><rect x="62" y="34" width="11" height="36"/><rect x="82" y="30" width="11" height="40"/><rect x="122" y="48" width="11" height="22"/><rect x="142" y="26" width="11" height="44"/><rect x="162" y="58" width="11" height="12"/><rect x="182" y="36" width="11" height="34"/><rect x="202" y="52" width="11" height="18"/><rect x="222" y="40" width="11" height="30"/></g>
      <rect x="102" y="20" width="11" height="50" fill="var(--green)"/>
      <g font-size="3" fill="#999"><text x="4" y="78">Jan</text><text x="24" y="78">Feb</text><text x="44" y="78">Mar</text><text x="64" y="78">Apr</text><text x="84" y="78">May</text><text x="104" y="78">Jun</text><text x="124" y="78">Jul</text><text x="144" y="78">Aug</text><text x="164" y="78">Sep</text><text x="184" y="78">Oct</text><text x="204" y="78">Nov</text><text x="224" y="78">Dec</text></g>
    </svg>
  </div>
  <div class="card" style="left:309px;top:586px;width:253px;height:122px">
    <div class="chart-label">Trading Volume ⌄</div>
    <svg class="abs" style="left:8px;top:28px" width="240" height="84" viewBox="0 0 240 84">
      <polyline fill="none" stroke="var(--green)" stroke-width="1" points="0,42 8,36 14,30 22,44 30,50 36,38 44,28 52,46 58,40 66,34 74,48 80,42 88,46 96,36 104,44 112,40 120,46 128,34 136,44 144,38 152,40 160,44 168,32 176,38 184,30 192,36 200,28 208,40 214,34 220,6 226,30"/>
      <g font-size="3" fill="#999"><text x="230" y="5">$20K</text><text x="230" y="18">$15.6K</text><text x="230" y="31">$10K</text><text x="230" y="44">$5K</text><text x="230" y="57">$1.5K</text><text x="230" y="70">$1K</text>
      <text x="0" y="82">00:00</text><text x="28" y="82">03:00</text><text x="56" y="82">06:00</text><text x="84" y="82">09:00</text><text x="112" y="82">12:00</text><text x="140" y="82">15:00</text><text x="168" y="82">18:00</text><text x="196" y="82">21:00</text><text x="222" y="82">24:00</text></g>
    </svg>
  </div>
  <div class="stat" style="left:42px;top:715px;width:126px;height:54px"><div class="k" style="font-size:5px;margin-top:12px">Exchanges Tracked</div><div class="v" style="font-size:17px;margin-top:4px">125</div></div>
  <div class="stat" style="left:173px;top:715px;width:126px;height:54px"><div class="k" style="font-size:5px;margin-top:12px">Average Trading Fee</div><div class="v" style="font-size:17px;margin-top:4px">0.15%</div></div>
  <div class="stat" style="left:304px;top:715px;width:126px;height:54px"><div class="k" style="font-size:5px;margin-top:12px">Total Users</div><div class="v" style="font-size:17px;margin-top:4px">828 M</div></div>
  <div class="stat" style="left:435px;top:715px;width:126px;height:54px"><div class="k" style="font-size:5px;margin-top:12px">Web Visitors</div><div class="v" style="font-size:17px;margin-top:4px">12.2 B</div></div>

  <h2 class="section-title" style="left:42px;top:788px;font-size:10px">Compare</h2>
  <div class="card" style="left:42px;top:811px;width:520px;height:357px">
    <svg class="abs" style="left:0;top:0" width="260" height="240" viewBox="0 0 260 240">
      <g transform="translate(126 135)" fill="none" stroke="#e2e2e2" stroke-width=".6">
        <polygon points="0,-90 85.6,-27.8 52.9,72.8 -52.9,72.8 -85.6,-27.8"/>
        <polygon transform="scale(.75)" points="0,-90 85.6,-27.8 52.9,72.8 -52.9,72.8 -85.6,-27.8"/>
        <polygon transform="scale(.5)" points="0,-90 85.6,-27.8 52.9,72.8 -52.9,72.8 -85.6,-27.8"/>
        <polygon transform="scale(.25)" points="0,-90 85.6,-27.8 52.9,72.8 -52.9,72.8 -85.6,-27.8"/>
        <path d="M0 0L0-90M0 0L85.6-27.8M0 0L52.9 72.8M0 0L-52.9 72.8M0 0L-85.6-27.8"/>
        <polygon points="0,-52 62,-20 34,44 -44,62 -74,-20" fill="#d6f0e6" stroke="#a9dcc7"/>
        <polygon points="0,-66 90,-22 14,-4 46,64 -30,-4" fill="#8fd2b6" fill-opacity=".85" stroke="#6cc39f"/>
      </g>
      <g font-size="4" fill="#444"><text x="118" y="40">Security</text><text x="222" y="104">Features</text><text x="188" y="221">Deposits</text><text x="42" y="220">Withdrawals</text><text x="22" y="101">Fees</text></g>
    </svg>
    <table class="radar-table" style="left:26px;top:240px;width:194px;font-size:4.5px">
      <tr><th style="height:14px"></th><th>Bintrove</th><th>Coinlane</th></tr>
      <tr><td style="height:16.5px">Fees</td><td>xyz</td><td>xyz</td></tr><tr><td style="height:16.5px">Security</td><td>xyz</td><td>xyz</td></tr><tr><td style="height:16.5px">Features</td><td>xyz</td><td>xyz</td></tr><tr><td style="height:16.5px">Deposits</td><td>xyz</td><td>xyz</td></tr><tr><td style="height:16.5px">Withdrawals</td><td>xyz</td><td>xyz</td></tr>
    </table>
    <div class="select" style="left:282px;top:38px;width:103px;height:21px;font-size:7px"><span>Bintrove</span><span>⌄</span></div>
    <div class="select" style="left:390px;top:38px;width:99px;height:21px;font-size:7px"><span>Coinlane</span><span>⌄</span></div>
    <div class="acc-head" style="left:286px;top:86px;width:200px;font-size:6px"><span>Top Picks</span><span>⌃</span></div>
    <div class="kv" style="left:286px;top:109px;width:196px;font-size:4.5px;row-gap:10px"><span># of Coins</span><span>xyz</span><span>xyz</span><span># of Futures</span><span>xyz</span><span>xyz</span><span>Trading Bots</span><span>xyz</span><span>xyz</span><span>Copy Bots</span><span>xyz</span><span>xyz</span><span>24/7 Support</span><span>xyz</span><span>xyz</span></div>
    <div class="divider" style="left:282px;top:195px;width:207px"></div>
    <div class="acc-head" style="left:286px;top:207px;width:200px;font-size:6px"><span>Security</span><span>⌄</span></div>
    <div class="acc-head" style="left:286px;top:231px;width:200px;font-size:6px"><span>Fees</span><span>⌄</span></div>
    <div class="acc-head" style="left:286px;top:254px;width:200px;font-size:6px"><span>Deposits</span><span>⌄</span></div>
    <div class="acc-head" style="left:286px;top:277px;width:200px;font-size:6px"><span>Withdrawals</span><span>⌄</span></div>
    <div class="see-all" style="left:282px;top:313px;width:207px;height:21px;font-size:6px">See All</div>
  </div>

  <div class="faq-zone" style="top:1194px;height:328px">
    <h2 class="section-title" style="left:42px;top:44px;font-size:10px">Frequently asked Question</h2>
    <div class="faq" style="left:42px;top:68px;width:520px;height:55px"><div class="q" style="left:20px;right:20px;top:16px;font-size:6.5px"><span>What are the Crypto Exchanges?</span><span>⌃</span></div><div class="a" style="left:20px;top:35px;font-size:6px">All current paused or on-hold postings will expire end of 2024.</div></div>
    <div class="faq" style="left:42px;top:130px;width:520px;height:76px"><div class="q" style="left:20px;right:20px;top:15px;font-size:6.5px"><span>How to choose Crypto Exchanges?</span><span>⌃</span></div><div class="a" style="left:20px;right:20px;top:34px;font-size:6px;line-height:10.5px">For confidential postings on Jobwell job page there's a $250 hosting fee (as well as other incurred fees) to use Arbor' account, which will include our team's search for possible candidates on these hiring platforms when purchasing Basic or Standard packages (this is included in Deluxe packages upon requested).</div></div>
    <div class="faq" style="left:42px;top:213px;width:520px;height:37px"><div class="q" style="left:20px;right:20px;top:14px;font-size:6.5px"><span>How is data tracked?</span><span>⌃</span></div></div>
    <div class="faq" style="left:42px;top:257px;width:520px;height:37px"><div class="q" style="left:20px;right:20px;top:14px;font-size:6.5px"><span>How often is data updated?</span><span>⌃</span></div></div>
  </div>
  <div class="footer" style="left:33px;right:33px;top:1535px;font-size:4.5px"><span>Privacy Policy</span><span>©2025 All rights reserved</span></div>
</section>

<!-- ================= MOBILE ================= -->
<section class="artboard mobile">
  <header class="site-header"><div class="logo">Brand Logo</div><div class="burger"></div></header>
  <div class="updated" style="left:9px;top:42px;font-size:4px">UPDATED: 22 FEB, 2025</div>
  <h1 class="title" style="left:9px;top:51px;font-size:12.5px;line-height:16px">COMPARE CRYPTO<br>EXCHANGES</h1>
  <div class="tracked" style="left:9px;top:89px;font-size:7px">Platform Tracked: <b>125</b></div>
  <div class="btn" style="left:9px;top:109px;width:67px;height:17px;font-size:4px">HOW WE TEST? <span>↗</span></div>
  <div class="rating-badge" style="left:116px;top:110px;width:36px;height:14px" role="img" aria-label="Review rating badge"></div>
  <h2 class="section-title" style="left:9px;top:150px;font-size:6px">Top Picks</h2>
  <div class="pick" style="left:9px;top:164px;width:145px;height:45px"><span class="name" style="left:9px;top:9px;font-size:8.5px">Vextra</span><svg class="arrow" style="right:9px;top:10px" width="10" height="10" viewBox="0 0 12 12"><path d="M2 10L10 2M4 2h6v6" stroke="#fff" stroke-width="1.4" fill="none"/></svg><div class="meta" style="left:9px;right:7px;bottom:7px;font-size:4px"><span>Trust score: 10/10</span><span>Go to the Platform</span></div></div>
  <div class="pick" style="left:9px;top:213px;width:145px;height:45px"><span class="name" style="left:9px;top:9px;font-size:8.5px">Coinlane</span><svg class="arrow" style="right:9px;top:10px" width="10" height="10" viewBox="0 0 12 12"><path d="M2 10L10 2M4 2h6v6" stroke="#fff" stroke-width="1.4" fill="none"/></svg><div class="meta" style="left:9px;right:7px;bottom:7px;font-size:4px"><span>Trust score: 10/10</span><span>Go to the Platform</span></div></div>
  <div class="pick" style="left:9px;top:262px;width:145px;height:45px"><span class="name" style="left:9px;top:9px;font-size:8.5px">Bintrove</span><svg class="arrow" style="right:9px;top:10px" width="10" height="10" viewBox="0 0 12 12"><path d="M2 10L10 2M4 2h6v6" stroke="#fff" stroke-width="1.4" fill="none"/></svg><div class="meta" style="left:9px;right:7px;bottom:7px;font-size:4px"><span>Trust score: 10/10</span><span>Go to the Platform</span></div></div>

  <div class="tools" style="left:9px;top:322px"><div class="tool" style="height:8px;font-size:3px;padding:0 3px">Fees ⌄</div></div>
  <div class="tools" style="right:9px;top:322px"><div class="tool" style="height:8px;font-size:3px;padding:0 3px">Columns ▯</div><div class="tool" style="height:8px;font-size:3px;padding:0 3px">Compare ⌄</div></div>
  <div class="table-card abs" style="left:9px;top:334px;width:145px">
    <table class="data-table" style="font-size:2.6px">
      <tr><th style="height:9px">Exchanges</th><th>Last Updated</th><th>Visit</th><th>Maker Fee</th><th>Taker Fee</th></tr>
      <tr><td style="height:11px"><i class="ex-dot" style="width:2px;height:2px"></i>Bintrove</td><td>25 Feb 2025</td><td class="site">Go to site</td><td>0.10%</td><td>0.20%</td></tr>
      <tr><td style="height:11px"><i class="ex-dot" style="width:2px;height:2px"></i>Byvault</td><td>25 Feb 2025</td><td class="site">Go to site</td><td>0.10%</td><td>0.20%</td></tr>
      <tr><td style="height:11px"><i class="ex-dot" style="width:2px;height:2px"></i>Coinlane</td><td>25 Feb 2025</td><td class="site">Go to site</td><td>0.10%</td><td>0.20%</td></tr>
      <tr><td style="height:11px"><i class="ex-dot" style="width:2px;height:2px"></i>Oktrix</td><td>25 Feb 2025</td><td class="site">Go to site</td><td>0.10%</td><td>0.20%</td></tr>
      <tr><td style="height:11px"><i class="ex-dot" style="width:2px;height:2px"></i>Upnest</td><td>25 Feb 2025</td><td class="site">Go to site</td><td>0.10%</td><td>0.20%</td></tr>
      <tr><td style="height:11px"><i class="ex-dot" style="width:2px;height:2px"></i>Vextra</td><td>25 Feb 2025</td><td class="site">Go to site</td><td>0.10%</td><td>0.20%</td></tr>
      <tr><td style="height:11px"><i class="ex-dot" style="width:2px;height:2px"></i>Kuvion</td><td>25 Feb 2025</td><td class="site">Go to site</td><td>0.10%</td><td>0.20%</td></tr>
    </table>
    <div class="table-foot" style="font-size:2.6px;padding:4px 5px"><span>Showing 1 to 7 of 120 Results</span></div>
  </div>

  <h2 class="section-title" style="left:9px;top:452px;font-size:6px">Compare</h2>
  <div class="card" style="left:9px;top:466px;width:145px;height:60px">
    <div class="chart-label" style="left:6px;top:5px;font-size:3px">Marker Fee ⌄</div>
    <svg class="abs" style="left:6px;top:14px" width="134" height="42" viewBox="0 0 240 80">
      <line x1="2" y1="7" x2="226" y2="7" stroke="#444" stroke-dasharray="3 3" stroke-width="1"/>
      <g fill="#dedede"><rect x="2" y="52" width="11" height="18"/><rect x="22" y="26" width="11" height="44"/><rect x="42" y="40" width="11" height="30"/><rect x="62" y="34" width="11" height="36"/><rect x="82" y="30" width="11" height="40"/><rect x="122" y="48" width="11" height="22"/><rect x="142" y="26" width="11" height="44"/><rect x="162" y="58" width="11" height="12"/><rect x="182" y="36" width="11" height="34"/><rect x="202" y="52" width="11" height="18"/><rect x="222" y="40" width="11" height="30"/></g>
      <rect x="102" y="20" width="11" height="50" fill="var(--green)"/>
    </svg>
  </div>
  <div class="card" style="left:9px;top:531px;width:145px;height:70px">
    <div class="chart-label" style="left:6px;top:5px;font-size:3px">Trading Volume ⌄</div>
    <svg class="abs" style="left:6px;top:14px" width="134" height="50" viewBox="0 0 240 84">
      <polyline fill="none" stroke="var(--green)" stroke-width="1.6" points="0,42 8,36 14,30 22,44 30,50 36,38 44,28 52,46 58,40 66,34 74,48 80,42 88,46 96,36 104,44 112,40 120,46 128,34 136,44 144,38 152,40 160,44 168,32 176,38 184,30 192,36 200,28 208,40 214,34 220,6 226,30"/>
    </svg>
  </div>
  <div class="stat" style="left:9px;top:606px;width:70px;height:40px"><div class="k" style="font-size:3.2px;margin-top:9px">Exchanges Tracked</div><div class="v" style="font-size:10px;margin-top:3px">125</div></div>
  <div class="stat" style="left:84px;top:606px;width:70px;height:40px"><div class="k" style="font-size:3.2px;margin-top:9px">Average Trading Fee</div><div class="v" style="font-size:10px;margin-top:3px">0.15%</div></div>
  <div class="stat" style="left:9px;top:651px;width:70px;height:40px"><div class="k" style="font-size:3.2px;margin-top:9px">Total Users</div><div class="v" style="font-size:10px;margin-top:3px">828 M</div></div>
  <div class="stat" style="left:84px;top:651px;width:70px;height:40px"><div class="k" style="font-size:3.2px;margin-top:9px">Web Visitors</div><div class="v" style="font-size:10px;margin-top:3px">12.2 B</div></div>

  <div class="card" style="left:9px;top:705px;width:145px;height:420px">
    <div class="select" style="left:5px;top:7px;width:64px;height:14px;font-size:4px;padding:0 4px"><span>Bintrove</span><span>⌄</span></div>
    <div class="select" style="left:74px;top:7px;width:66px;height:14px;font-size:4px;padding:0 4px"><span>Coinlane</span><span>⌄</span></div>
    <div class="acc-head" style="left:7px;top:33px;width:131px;font-size:4px"><span>Top Picks</span><span>⌃</span></div>
    <div class="kv" style="left:7px;top:47px;width:127px;font-size:3px;row-gap:6px"><span># of Coins</span><span>xyz</span><span>xyz</span><span># of Futures</span><span>xyz</span><span>xyz</span><span>Trading Bots</span><span>xyz</span><span>xyz</span><span>Copy Bots</span><span>xyz</span><span>xyz</span><span>24/7 Support</span><span>xyz</span><span>xyz</span></div>
    <div class="acc-head" style="left:7px;top:114px;width:131px;font-size:4px"><span>Security</span><span>⌄</span></div>
    <div class="acc-head" style="left:7px;top:131px;width:131px;font-size:4px"><span>Fees</span><span>⌄</span></div>
    <div class="acc-head" style="left:7px;top:148px;width:131px;font-size:4px"><span>Deposits</span><span>⌄</span></div>
    <div class="acc-head" style="left:7px;top:165px;width:131px;font-size:4px"><span>Withdrawals</span><span>⌄</span></div>
    <div class="see-all" style="left:5px;top:185px;width:135px;height:13px;font-size:4px">See All</div>
    <svg class="abs" style="left:0;top:205px" width="145" height="135" viewBox="0 0 260 240">
      <g transform="translate(126 120)" fill="none" stroke="#e2e2e2" stroke-width="1">
        <polygon points="0,-90 85.6,-27.8 52.9,72.8 -52.9,72.8 -85.6,-27.8"/>
        <polygon transform="scale(.66)" points="0,-90 85.6,-27.8 52.9,72.8 -52.9,72.8 -85.6,-27.8"/>
        <polygon transform="scale(.33)" points="0,-90 85.6,-27.8 52.9,72.8 -52.9,72.8 -85.6,-27.8"/>
        <polygon points="0,-52 62,-20 34,44 -44,62 -74,-20" fill="#d6f0e6" stroke="#a9dcc7"/>
        <polygon points="0,-66 90,-22 14,-4 46,64 -30,-4" fill="#8fd2b6" fill-opacity=".85" stroke="#6cc39f"/>
      </g>
      <g font-size="7" fill="#444"><text x="112" y="22">Security</text><text x="216" y="92">Features</text><text x="182" y="206">Deposits</text><text x="30" y="206">Withdrawals</text><text x="18" y="90">Fees</text></g>
    </svg>
    <table class="radar-table" style="left:7px;top:343px;width:131px;font-size:2.8px">
      <tr><th style="height:8px"></th><th>Bintrove</th><th>Coinlane</th></tr>
      <tr><td style="height:10px">Fees</td><td>xyz</td><td>xyz</td></tr><tr><td style="height:10px">Security</td><td>xyz</td><td>xyz</td></tr><tr><td style="height:10px">Features</td><td>xyz</td><td>xyz</td></tr><tr><td style="height:10px">Deposits</td><td>xyz</td><td>xyz</td></tr><tr><td style="height:10px">Withdrawals</td><td>xyz</td><td>xyz</td></tr>
    </table>
  </div>

  <div class="faq-zone" style="top:1140px;height:240px">
    <h2 class="section-title" style="left:9px;top:14px;font-size:5.5px">Frequently asked Question</h2>
    <div class="faq" style="left:9px;top:31px;width:145px;height:42px"><div class="q" style="left:7px;right:7px;top:9px;font-size:4px"><span>What are the Crypto Exchanges?</span><span>⌃</span></div><div class="a" style="left:7px;right:7px;top:21px;font-size:3px;line-height:5px">All current paused or on-hold postings will expire end of 2024.</div></div>
    <div class="faq" style="left:9px;top:82px;width:145px;height:75px"><div class="q" style="left:7px;right:7px;top:9px;font-size:4px"><span>How to choose Crypto Exchanges?</span><span>⌃</span></div><div class="a" style="left:7px;right:7px;top:21px;font-size:3px;line-height:5.2px">For confidential postings on Jobwell job page there's a $250 hosting fee (as well as other incurred fees) to use Arbor' account, which will include our team's search for possible candidates on these hiring platforms when purchasing Basic or Standard packages (this is included in Deluxe packages upon requested).</div></div>
    <div class="faq" style="left:9px;top:165px;width:145px;height:23px"><div class="q" style="left:7px;right:7px;top:9px;font-size:4px"><span>How is data tracked?</span><span>⌃</span></div></div>
    <div class="faq" style="left:9px;top:193px;width:145px;height:23px"><div class="q" style="left:7px;right:7px;top:9px;font-size:4px"><span>How often is data updated?</span><span>⌃</span></div></div>
  </div>
  <div class="footer" style="left:10px;right:10px;top:1384px;font-size:3px"><span>Privacy Policy</span><span>©2025 All rights reserved</span></div>
</section>

</div>
</body>
</html>
```